web design needed for brivolent safety ltd

We need a web design for our new company. It is called Brivo Lent Safety Ltd and is a company based around a security/safety/info box specifically made for on construction sites, but could be used elsewhere. It is completely portable with a builtin alarm system with remote. There is a larger box and a smaller box (only have an image for this one at this stage, I will get better photos of the temp box soon, but this one will make a start).
This will be the standard box that is for sale, howver you can get upgrades that include a fire extinguisher, first aid kit, hand sanitizer, fire blanket.
Other features include a place for plans and safety info for the site, a hook attached to the back of the smaller box so it can be hung on the door. Both boxes are suitable for outside.
We would like the wesite to incorporate our logo and pictures of the box. I have attached our logo and an exaple of a mock box as the final box is still being made sothese photos will be swapped once we have it from the manufacturer.
We would like the following pages:
Home (possibly a picture of the box rotating, doesnt have to though?)
About us
Products
FAQ
Shopping cart
Contact us
We would like the style to be crisp, simple and not to busy.
Thanks
Updates
More photos of the box have been added. These are for the larger box.
Reason: we are happy to give people more time so have extended it by seven days
Target Market(s)
Builders mainly
Industry/Entity Type
Construction
Font styles to use
Other font styles liked:
- ERAS BOLD ITC
Look and feel
Each slider illustrates characteristics of the customer's brand and the style your logo design should communicate.

```html
<!DOCTYPE html>
<html lang="en">
<head>
<meta charset="utf-8">
<title>Halvenor Safety</title>
<link rel="stylesheet" href="https://fonts.googleapis.com/css2?family=Ubuntu:wght@500;700&family=Open+Sans:wght@400;600;700&display=swap">
<style>
:root{
  --page:#1f1f1f;
  --header:#3d3d3d;
  --band:#272727;
  --footer:#1c1c1c;
  --nav:#2b2b2b;
  --nav-line:#3a3a3a;
  --green:#8dc63f;
  --blue:#3aa6d0;
  --white:#ffffff;
  --text:#9a9a9a;
  --muted:#7a7a7a;
  --card:#f1f1f1;
  --card-text:#555555;
}
*{box-sizing:border-box;margin:0;padding:0}
html,body{width:1200px;height:1200px;overflow:hidden}
body{background:var(--page);font-family:"Open Sans",Arial,sans-serif;color:var(--text);position:relative}
.abs{position:absolute}
.heading{font-family:"Ubuntu",Arial,sans-serif;font-weight:700;color:var(--white);text-transform:uppercase}

.site-header{left:0;top:0;width:1200px;height:118px;background:linear-gradient(#454545,#393939)}
.brand-mark{left:275px;top:34px;width:42px;height:42px;background:var(--green);border-radius:6px}
.brand-name{left:322px;top:46px;font-size:17px;letter-spacing:.3px;white-space:nowrap}
.account{right:272px;top:68px;font-size:8px;font-weight:700;color:#cfcfcf;white-space:nowrap}
.account .login{color:var(--blue)}
.cart-summary{right:272px;top:82px;font-size:8px;font-weight:700;color:#bdbdbd;display:flex;align-items:center;gap:6px;white-space:nowrap}

.main-nav{left:275px;top:97px;width:655px;height:40px;background:var(--nav);display:flex}
.main-nav a{height:40px;line-height:40px;text-align:center;font-size:9.5px;font-weight:700;color:#e8e8e8;text-decoration:none;border-right:1px solid var(--nav-line);white-space:nowrap}
.main-nav a.active{background:var(--green);color:#1d1d1d}
.search{left:790px;top:106px;width:133px;height:25px;background:#4a4a4a;display:flex;align-items:center;gap:8px;padding-left:10px;font-size:8px;color:#a8a8a8}

.hero{left:275px;top:137px;width:655px;height:260px;background:linear-gradient(100deg,#5a5a5a,#8a8a8a 45%,#6f6f6f 70%,#9a9a9a)}
.caption{left:661px;top:265px;width:229px;height:87px;background:rgba(38,38,38,.92);padding:14px 26px}
.caption::before{content:"";position:absolute;left:19px;top:0;border:10px solid transparent;border-top:9px solid var(--green);border-bottom:0}
.caption h2{font-size:12.5px;margin-bottom:7px;white-space:nowrap}
.caption p{font-size:7.5px;line-height:14px;color:#9c9c9c}
.caption em{font-style:normal;color:var(--green)}
.slide-prev,.slide-next{top:352px;width:33px;height:33px;display:flex;align-items:center;justify-content:center}
.slide-prev{left:661px;background:#3a3a3a}
.slide-next{left:694px;background:var(--green)}

.promo-band{left:275px;top:397px;width:655px;height:121px;background:var(--blue)}
.promo{top:414px;width:300px;height:88px;background:#262626;display:flex}
.promo .copy{width:154px;padding:20px 10px;font-size:7.5px;line-height:11px;color:#aaa;position:relative}
.promo .copy.lit{color:var(--blue)}
.promo .copy::after{content:"";position:absolute;right:-6px;top:18px;border:6px solid transparent;border-left:6px solid #262626;border-right:0}
.promo .link{display:block;margin-top:12px;font-size:7.5px}
.promo .link.white{color:#fff;text-decoration:underline}
.promo .link.blue{color:var(--blue)}
.promo .photo{flex:1;background:linear-gradient(135deg,#707070,#9c9c9c 60%,#b4b4b4)}

.section-title{left:275px;top:565px;font-size:13px}
.section-rule{left:380px;top:578px;width:530px;height:1px;background:#3b3b3b}
.section-more{left:918px;top:566px}

.product{top:598px;width:148px;height:187px;background:var(--card)}
.product .photo{height:103px}
.product h3{font-size:7.5px;font-weight:400;line-height:13px;color:var(--card-text);padding:8px 11px 0;text-transform:uppercase}
.product .price{position:absolute;left:11px;top:160px;font-size:10px;font-weight:700}
.product .add{position:absolute;right:10px;top:157px;width:26px;height:20px;display:flex;align-items:center;justify-content:center}

.info-band{left:0;top:812px;width:1200px;height:206px;background:var(--band)}
.info-title{top:849px;font-size:10px}
.about-lead{left:275px;top:886px;font-size:6.5px;font-weight:700;color:var(--green);text-transform:uppercase;white-space:nowrap}
.about-copy{left:275px;top:906px;font-size:7.5px;line-height:14px;white-space:nowrap}
.divider{left:561px;top:854px;width:1px;height:132px;background:#3a3a3a}
.date-day{left:616px;top:870px;font-family:"Open Sans",Arial,sans-serif;font-weight:600;font-size:55px;color:var(--green);line-height:1}
.date-month{left:618px;top:936px;font-size:24px;color:#8a8a8a;line-height:1}
.news-head{left:686px;top:886px;font-size:7px;font-weight:700;line-height:13px;color:#ddd;text-transform:uppercase;white-space:nowrap}
.news-copy{left:686px;top:920px;font-size:7.5px;line-height:14px;white-space:nowrap}
.view-all{left:688px;top:969px;font-size:6.5px;color:#aaa;text-decoration:underline}

.site-footer{left:0;top:1018px;width:1200px;height:182px;background:var(--footer)}
.foot-title{top:1061px;font-size:10px}
.signup{left:275px;top:1087px;font-size:7.5px;color:#aaa}
.email-field{left:275px;top:1109px;width:123px;height:24px;background:#3a3a3a}
.email-send{left:398px;top:1109px;width:28px;height:24px;background:var(--green);display:flex;align-items:center;justify-content:center}
.social{top:1142px;width:24px;height:24px;background:#3a3a3a}
.link-list{top:1088px;list-style:none;font-size:6.8px;line-height:13.2px;color:#8a8a8a;text-transform:uppercase}
.copyright{left:275px;top:1180px;font-size:6.3px;color:#777}
</style>
</head>
<body>

<header class="site-header abs"></header>
<div class="brand-mark abs"></div>
<div class="brand-name abs heading">Halvenor Safety</div>
<div class="account abs">My Account &nbsp;|&nbsp; <span class="login">Login</span></div>
<div class="cart-summary abs">
  <svg width="11" height="9" viewBox="0 0 11 9"><path d="M0 1h2l1.5 5h6L11 2H3" fill="none" stroke="#bdbdbd" stroke-width="1.2"/><circle cx="4" cy="8" r=".9" fill="#bdbdbd"/><circle cx="9" cy="8" r=".9" fill="#bdbdbd"/></svg>
  MY CART: 0 ITEM(S) - $0.00
  <svg width="8" height="5" viewBox="0 0 8 5"><path d="M0 0l4 5 4-5z" fill="#777"/></svg>
</div>

<nav class="main-nav abs">
  <a class="active" style="width:65px">Home</a>
  <a style="width:71px">About Us</a>
  <a style="width:67px">Products</a>
  <a style="width:61px">FAQ</a>
  <a style="width:90px">Shipping Cart</a>
  <a style="width:78px">Contact Us</a>
</nav>
<div class="search abs">
  <svg width="10" height="10" viewBox="0 0 10 10"><circle cx="4" cy="4" r="3" fill="none" stroke="#ccc" stroke-width="1.5"/><path d="M6.3 6.3L9.5 9.5" stroke="#ccc" stroke-width="1.6"/></svg>
  Search
</div>

<div class="hero abs" role="img" aria-label="Photo of the safety box on site with a fire extinguisher beside it"></div>
<div class="caption abs">
  <h2 class="heading" style="text-transform:none">Lorem ipsum dolor sit</h2>
  <p>Lorem ipsum dolor sit amet, consectetur adipisicing elit, sed do <em>eiusmod tempor incididunt</em> ut labore et dolore magna aliqua.</p>
</div>
<div class="slide-prev abs"><svg width="8" height="14" viewBox="0 0 8 14"><path d="M7 1L1 7l6 6" fill="none" stroke="#666" stroke-width="1.5"/></svg></div>
<div class="slide-next abs"><svg width="8" height="14" viewBox="0 0 8 14"><path d="M1 1l6 6-6 6" fill="none" stroke="#cfe8a8" stroke-width="1.5"/></svg></div>

<div class="promo-band abs"></div>
<div class="promo abs" style="left:292px">
  <div class="copy lit">Lorem ipsum dolor sit amet, consectetur adipisicing elit Lorem ipsum dolor sit amet,<span class="link white">Lorem ipsum dolor</span></div>
  <div class="photo" role="img" aria-label="Photo of the safety box door"></div>
</div>
<div class="promo abs" style="left:610px">
  <div class="copy">Lorem ipsum dolor sit amet, consectetur adipisicing elit Lorem ipsum dolor sit amet,<span class="link blue">Lorem ipsum dolor</span></div>
  <div class="photo" role="img" aria-label="Photo of the safety box door"></div>
</div>

<h2 class="section-title abs heading">Lorem Ipsum</h2>
<div class="section-rule abs"></div>
<svg class="section-more abs" width="10" height="10" viewBox="0 0 10 10"><path d="M1 1l4 4-4 4M5 1l4 4-4 4" fill="none" stroke="#999" stroke-width="1.2"/></svg>

<div class="product abs" style="left:275px">
  <div class="photo" role="img" aria-label="Photo of lockers with keys" style="background:linear-gradient(135deg,#8a8a78,#b7b39c)"></div>
  <h3>16 channel real-time DVR<br>security system with 2TB<br>HDD &amp; 16 700TVL</h3>
  <span class="price" style="color:var(--green)">$1,450.00</span>
  <span class="add" style="background:var(--blue)"><svg width="13" height="11" viewBox="0 0 11 9"><path d="M0 1h2l1.5 5h6L11 2H3" fill="none" stroke="#fff" stroke-width="1.2"/><circle cx="4" cy="8" r=".9" fill="#fff"/><circle cx="9" cy="8" r=".9" fill="#fff"/></svg></span>
</div>
<div class="product abs" style="left:445px">
  <div class="photo" role="img" aria-label="Photo of a digital keypad safe" style="background:linear-gradient(135deg,#6e6a62,#3a3a3a 60%,#5c5a55)"></div>
  <h3>16 channel real-time DVR<br>security system with 2TB</h3>
  <span class="price" style="color:var(--blue)">$1,450.00</span>
  <span class="add" style="background:var(--green)"><svg width="13" height="11" viewBox="0 0 11 9"><path d="M0 1h2l1.5 5h6L11 2H3" fill="none" stroke="#fff" stroke-width="1.2"/><circle cx="4" cy="8" r=".9" fill="#fff"/><circle cx="9" cy="8" r=".9" fill="#fff"/></svg></span>
</div>
<div class="product abs" style="left:612px">
  <div class="photo" role="img" aria-label="Photo of a small dial safe" style="background:linear-gradient(135deg,#f4f4f4,#a6ab9a 50%,#6d706a)"></div>
  <h3>16 channel real-time DVR<br>security system with 2TB<br>HDD &amp; 16 700TVL</h3>
  <span class="price" style="color:var(--blue)">$1,450.00</span>
  <span class="add" style="background:var(--green)"><svg width="13" height="11" viewBox="0 0 11 9"><path d="M0 1h2l1.5 5h6L11 2H3" fill="none" stroke="#fff" stroke-width="1.2"/><circle cx="4" cy="8" r=".9" fill="#fff"/><circle cx="9" cy="8" r=".9" fill="#fff"/></svg></span>
</div>
<div class="product abs" style="left:779px">
  <div class="photo" role="img" aria-label="Photo of a black safe with dial and handle" style="background:linear-gradient(135deg,#2a2a2a,#3b3a33 60%,#1f1f1f)"></div>
  <h3>16 channel real-time DVR<br>security system with 2TB<br>HDD &amp; 16 700TVL</h3>
  <span class="price" style="color:var(--blue)">$1,450.00</span>
  <span class="add" style="background:var(--green)"><svg width="13" height="11" viewBox="0 0 11 9"><path d="M0 1h2l1.5 5h6L11 2H3" fill="none" stroke="#fff" stroke-width="1.2"/><circle cx="4" cy="8" r=".9" fill="#fff"/><circle cx="9" cy="8" r=".9" fill="#fff"/></svg></span>
</div>

<section class="info-band abs"></section>
<h2 class="info-title abs heading" style="left:275px">About Us</h2>
<p class="about-lead abs">Lorem ipsum dolor sit amet, consectetur adipisicing elit</p>
<p class="about-copy abs">Lorem ipsum dolor sit amet, consectetur adipisicing elit, sed do eius-<br>mod tempor incididunt ut labore et dolore magna aliqua. Ut enim ad<br>minim veniam, quis nostrud exercitation ullamco laboris nisi ut aliquip<br>ex ea commodo consequat. [...]</p>
<div class="divider abs"></div>
<h2 class="info-title abs heading" style="left:618px">News &amp; Events</h2>
<div class="date-day abs">21</div>
<div class="date-month abs">JULY</div>
<p class="news-head abs">Lorem ipsum dolor sit amet, consec-<br>tetur adipisicing elit</p>
<p class="news-copy abs">Ut enim ad minim veniam, quis nostrud exercitation<br>ullamco laboris nisi ut aliquip ex ea commodo con-<br>sequat. Duis aute irure</p>
<span class="view-all abs">view all &gt;&gt;</span>

<footer class="site-footer abs"></footer>
<h2 class="foot-title abs heading" style="left:275px">Newsletter</h2>
<p class="signup abs">SIGN UP FOR OUR NEWSLETTER:</p>
<div class="email-field abs"></div>
<div class="email-send abs"><svg width="6" height="10" viewBox="0 0 6 10"><path d="M1 1l4 4-4 4" fill="none" stroke="#fff" stroke-width="1.3"/></svg></div>
<div class="social abs" style="left:275px" aria-label="Social link"></div>
<div class="social abs" style="left:305px" aria-label="Social link"></div>
<div class="social abs" style="left:336px" aria-label="Social link"></div>
<div class="social abs" style="left:366px" aria-label="Social link"></div>
<p class="copyright abs">Copyright© 2014 Company Name . All rights reserved</p>

<h2 class="foot-title abs heading" style="left:505px">Site Info</h2>
<ul class="link-list abs" style="left:505px"><li>Home</li><li>About us</li><li>Products</li><li>FAQ</li><li>Contact us</li></ul>
<h2 class="foot-title abs heading" style="left:636px">Other Links</h2>
<ul class="link-list abs" style="left:636px"><li>Lorem ipsum</li><li>Lorem ipsum dolor</li><li>Lorem ipsum dolor</li><li>Lorem ips dolor</li><li>Lorem ipsum</li></ul>
<h2 class="foot-title abs heading" style="left:782px">Other Links</h2>
<ul class="link-list abs" style="left:782px"><li>Lorem ipsum</li><li>Lorem ipsum dolor</li><li>Lorem ipsum dolor</li><li>Lorem ips dolor</li><li>Lorem ipsum</li></ul>

</body>
</html>
```